Chat Software Business Card Design

We need a business card design for our company.

We provide businesses with a platform to communicate with their web visitors in real time using chat boxes on their web sites.

We're using a bright color scheme to attract attention on the site and the business card would do well to reflect this also to maintain brand awareness. However it is not essential to the ultimate design to use the same color scheme or feel as the site.

We offer a Free Trial of the software and would encourage a business card design to promote this if possible.

http://qelmarworks7.co.uk/projects/guest/index2.html

You will find the company logo attached also.

An eye catching design with something that will set the card apart from others is required.

The design of the card/theme of the card should be very unique, setting our selves apart, eye catching whilst not providing a "wacky" image for the company.

It should also include our contact information;~
Website - www.talkpond-live.com
Email - support@talkpond-live.com
Twitter - @Talkpondlive

Industry/Entity Type

Software

Contact Information for Business Card

Web - www.talkpond-live.com
Email - office@talkpond-live.com
Skype - Talkpond.Live

Requirements
Must have
• Use of company logo is required.

```html
<!DOCTYPE html>
<html lang="en">
<head>
<meta charset="utf-8">
<title>Talkpond Live – Business Card</title>
<link rel="stylesheet" href="https://fonts.googleapis.com/css2?family=Share+Tech+Mono&display=swap">
<style>
  :root {
    --page-bg: #d8d5cf;
    --card-bg: #efede9;
    --brand-orange: #e55d2b;
    --brand-yellow: #f5b14a;
    --card-shadow: rgba(40, 30, 20, 0.18);
  }
  * { margin: 0; padding: 0; box-sizing: border-box; }
  html, body {
    width: 1200px;
    height: 1000px;
    overflow: hidden;
    background: var(--page-bg);
  }
  .stage {
    width: 1200px;
    height: 1000px;
    display: flex;
    align-items: center;
    justify-content: center;
  }
  .business-card {
    position: relative;
    width: 900px;
    height: 514px;
    background: var(--card-bg);
    border-radius: 6px;
    overflow: hidden;
    box-shadow: 0 18px 40px var(--card-shadow);
    font-family: "Share Tech Mono", monospace;
    color: var(--brand-orange);
  }
  .card-waves {
    position: absolute;
    inset: 0;
    width: 100%;
    height: 100%;
  }
  .wave-yellow { fill: var(--brand-yellow); }
  .wave-orange { fill: var(--brand-orange); }

  .brand {
    position: absolute;
    left: 52px;
    top: 108px;
    display: flex;
    align-items: center;
    gap: 14px;
  }
  .brand-mark {
    width: 34px;
    height: 34px;
    background: var(--brand-orange);
    border-radius: 4px;
  }
  .brand-name {
    font-size: 46px;
    letter-spacing: 1px;
    color: var(--brand-orange);
  }

  .contact-list {
    position: absolute;
    left: 470px;
    top: 52px;
    list-style: none;
  }
  .contact-item {
    display: flex;
    align-items: center;
    gap: 14px;
    height: 46px;
    font-size: 22px;
    letter-spacing: 1.5px;
  }
  .contact-icon {
    width: 26px;
    height: 26px;
    flex: none;
  }
  .contact-icon .stroke {
    fill: none;
    stroke: var(--brand-orange);
    stroke-width: 2;
  }
  .contact-icon .solid { fill: var(--brand-orange); }
</style>
</head>
<body>
<main class="stage">
  <article class="business-card">
    <svg class="card-waves" viewBox="0 0 900 514" preserveAspectRatio="none" aria-hidden="true">
      <path class="wave-yellow" d="M0,292 C260,360 560,365 900,238 L900,514 L0,514 Z"/>
      <path class="wave-orange" d="M0,382 C320,425 630,330 900,212 L900,514 L0,514 Z"/>
    </svg>

    <div class="brand">
      <span class="brand-mark" aria-hidden="true"></span>
      <span class="brand-name">Talkpond Live</span>
    </div>

    <ul class="contact-list">
      <li class="contact-item">
        <svg class="contact-icon" viewBox="0 0 26 26" aria-hidden="true">
          <circle class="stroke" cx="13" cy="13" r="11"/>
          <ellipse class="stroke" cx="13" cy="13" rx="5" ry="11"/>
          <line class="stroke" x1="2" y1="13" x2="24" y2="13"/>
        </svg>
        <span>www.talkpond-live.com</span>
      </li>
      <li class="contact-item">
        <svg class="contact-icon" viewBox="0 0 26 26" aria-hidden="true">
          <rect class="solid" x="2" y="6" width="22" height="15" rx="1"/>
          <polyline points="3,7 13,15 23,7" fill="none" stroke="var(--card-bg)" stroke-width="2"/>
        </svg>
        <span>office@talkpond-live.com</span>
      </li>
      <li class="contact-item">
        <svg class="contact-icon" viewBox="0 0 26 26" aria-hidden="true">
          <circle class="solid" cx="13" cy="13" r="11"/>
        </svg>
        <span>Talkpond.Live</span>
      </li>
      <li class="contact-item">
        <svg class="contact-icon" viewBox="0 0 26 26" aria-hidden="true">
          <circle class="solid" cx="13" cy="13" r="11"/>
        </svg>
        <span>@Talkpondlive</span>
      </li>
    </ul>
  </article>
</main>
</body>
</html>
```